PLUM BUSINESS CARD

Need a business card and logo. The company name is PLUM (Piedmont League of Ultimate Mareriders). It's a business that offers horseback riding lessons to young girls. Please put my name: Renata Bowley and a place for email and phone number. I would like the card to look feminine and soft. I like script type lettering. I want the card to be white or ivory with black or gray and hot pink print. A horse head outline would be cool, something whimsical. Think teen girl who likes glamour. Also, I give western riding lessons. So I like faded out background Images of western saddles, cowgirls, horses with long hair, ropes, horses in sunset...mabe the word PLUM can be made out of a lasso rope?

Just updated my project with a little more detail

Target Market(s)

Young girls/ cowgirls, western riding

Industry/Entity Type

Horseback Riding

Font styles to use
Script

Colors
e34197

Requirements
Must have
• A logo of PLUM.
Must say Piedmont League of Ultimate Mareriders
Colors are Pink and Black with an elegant, glamorous, feminine look.
Nice to have
• Could have a picture or outline of a horse

```html
<!DOCTYPE html>
<html lang="en">
<head>
<meta charset="utf-8">
<title>PLUM Business Card</title>
<link rel="stylesheet" href="https://fonts.googleapis.com/css2?family=Gentium+Book+Plus&family=Courgette&display=swap">
<style>
  :root {
    --hot-pink: #e34197;
    --pink-soft: #c93a86;
    --card-black: #121112;
    --card-black-2: #1a191a;
    --ghost: #2a2829;
    --text-light: #bdbcbc;
    --text-mid: #9a9899;
    --backdrop: #e4e4e4;
  }
  * { box-sizing: border-box; margin: 0; padding: 0; }
  html, body {
    width: 1200px;
    height: 926px;
    overflow: hidden;
    background: var(--backdrop);
  }
  .sheet {
    width: 1200px;
    height: 926px;
    display: flex;
    flex-direction: column;
    align-items: center;
    justify-content: center;
    gap: 50px;
  }
  .card {
    position: relative;
    width: 660px;
    height: 404px;
    overflow: hidden;
    background-color: var(--card-black);
    background-image:
      repeating-linear-gradient(0deg, rgba(255,255,255,0.018) 0 1px, transparent 1px 3px),
      repeating-linear-gradient(90deg, rgba(255,255,255,0.018) 0 1px, transparent 1px 3px),
      radial-gradient(ellipse at 40% 40%, var(--card-black-2), var(--card-black));
    box-shadow: 0 6px 18px rgba(0,0,0,0.25);
    font-family: "Gentium Book Plus", Georgia, serif;
  }
  .brand-disc {
    position: absolute;
    border-radius: 50%;
    background: var(--hot-pink);
    display: flex;
    align-items: center;
    justify-content: center;
  }
  .brand-name {
    font-family: "Gentium Book Plus", Georgia, serif;
    color: var(--card-black);
    letter-spacing: 1px;
  }
  /* Contact side */
  .card--contact .brand-disc { left: 8px; top: -4px; width: 104px; height: 104px; }
  .card--contact .brand-name { font-size: 26px; }
  .org-title {
    position: absolute;
    left: 128px;
    top: 30px;
    color: var(--text-light);
    font-size: 23px;
    line-height: 1.1;
  }
  .holder-name {
    position: absolute;
    left: 32px;
    top: 134px;
    font-family: "Courgette", cursive;
    font-weight: 400;
    color: var(--hot-pink);
    font-size: 38px;
  }
  .contact-list {
    position: absolute;
    left: 34px;
    top: 208px;
    list-style: none;
    color: var(--text-mid);
    font-size: 17px;
  }
  .contact-list li {
    display: flex;
    align-items: center;
    gap: 12px;
    height: 30px;
  }
  .contact-list svg { width: 14px; height: 14px; fill: none; stroke: var(--hot-pink); stroke-width: 1.6; }
  .ghost-art {
    position: absolute;
    left: 395px;
    top: 130px;
    width: 235px;
    height: 240px;
    border-radius: 40% 30% 10% 20%;
    background: radial-gradient(ellipse at 50% 45%, var(--ghost), rgba(42,40,41,0) 72%);
  }
  .accent-band {
    position: absolute;
    left: 0;
    bottom: 30px;
    width: 100%;
    height: 30px;
    background: var(--hot-pink);
  }
  /* Brand side */
  .card--brand .brand-disc { left: 22px; top: -4px; width: 112px; height: 112px; }
  .card--brand .brand-name { font-size: 28px; }
  .hero-art {
    position: absolute;
    left: 300px;
    top: 40px;
    width: 230px;
    height: 220px;
    border-radius: 45% 40% 20% 30%;
    background: radial-gradient(ellipse at 50% 45%, var(--hot-pink), var(--pink-soft) 55%, rgba(201,58,134,0) 75%);
  }
  .org-title--pink {
    position: absolute;
    left: 80px;
    right: 30px;
    top: 280px;
    text-align: center;
    color: var(--hot-pink);
    font-size: 25px;
  }
</style>
</head>
<body>
<main class="sheet">
  <section class="card card--brand">
    <div class="brand-disc"><span class="brand-name">PLUM</span></div>
    <div class="hero-art" role="img" aria-label="Whimsical swirled horse head illustration in hot pink"></div>
    <p class="org-title--pink">Piedmont League of Ultimate Mareriders</p>
  </section>

  <section class="card card--contact">
    <div class="brand-disc"><span class="brand-name">PLUM</span></div>
    <p class="org-title">Piedmont League of<br>Ultimate Mareriders</p>
    <h1 class="holder-name">Renata Bowley</h1>
    <ul class="contact-list">
      <li>
        <svg viewBox="0 0 16 16" aria-hidden="true"><path d="M3 2h3l1 3-2 1.5a8 8 0 0 0 4.5 4.5L11 9l3 1v3a1 1 0 0 1-1 1A11 11 0 0 1 2 3a1 1 0 0 1 1-1z"/></svg>
        <span>0400 918 276</span>
      </li>
      <li>
        <svg viewBox="0 0 16 16" aria-hidden="true"><rect x="1.5" y="3.5" width="13" height="9"/><path d="M1.5 3.5 8 9l6.5-5.5"/></svg>
        <span>renata@plumriders.com.au</span>
      </li>
    </ul>
    <div class="ghost-art" role="img" aria-label="Faint swirled horse head illustration in dark grey"></div>
    <div class="accent-band"></div>
  </section>
</main>
</body>
</html>
```